Looking to update current business card

We have a two sided card currently that needs a fresher, newer look. I like the fact it has two sides with a list of products/services we offer on the back side but the overall front look is lackluster. Our logo will stay the same.. I just want someone to bring some new life into the business card.

I like cards that have rounded corners but not sure if there's enough room?

Attached is our current biz card design and logo.

Target Market(s)

business customers

Industry/Entity Type

Business

Contact Information for Business Card

see above

```html
<!DOCTYPE html>
<html lang="en">
<head>
<meta charset="utf-8">
<title>Harbor Shield Systems – Business Card</title>
<link href="https://fonts.googleapis.com/css2?family=Arimo:wght@400;700&display=swap" rel="stylesheet">
<style>
  :root {
    --navy: #2d5a87;
    --orange: #f07f3c;
    --grey: #7a7a7a;
    --rule: #9a9a9a;
    --ink: #222222;
    --paper: #ffffff;
    --backdrop: #e9e7e4;
  }
  html, body {
    margin: 0;
    padding: 0;
    overflow: hidden;
  }
  body {
    width: 1200px;
    height: 873px;
    background: var(--backdrop);
    font-family: "Arimo", Arial, sans-serif;
    position: relative;
  }
  .card {
    position: absolute;
    background: var(--paper);
    box-shadow: 0 4px 14px rgba(0,0,0,0.15);
    overflow: hidden;
  }

  /* Back side: services list */
  .card-back {
    left: 106px;
    top: 148px;
    width: 330px;
    height: 578px;
  }
  .back-frame {
    position: absolute;
    inset: 18px;
    border: 2px solid var(--rule);
  }
  .services-title {
    margin: 34px 0 0;
    text-align: center;
    color: var(--orange);
    font-weight: 700;
    font-size: 15px;
    text-decoration: underline;
    text-underline-offset: 3px;
  }
  .services-list {
    list-style: none;
    margin: 22px 0 0;
    padding: 0;
    text-align: center;
    color: var(--grey);
    font-size: 13px;
    line-height: 27.5px;
  }
  .back-footer {
    position: absolute;
    left: 0;
    right: 0;
    top: 392px;
    border-top: 2px solid var(--rule);
    text-align: center;
    padding-top: 60px;
  }
  .company-name {
    color: var(--navy);
    font-weight: 700;
    font-size: 14px;
    letter-spacing: 2.4px;
    margin: 0;
  }
  .company-address {
    margin: 6px 0 0;
    font-style: normal;
    color: var(--ink);
    font-size: 13px;
    line-height: 16px;
  }
  .back-base {
    position: absolute;
    left: 0;
    right: 0;
    bottom: 0;
    height: 64px;
    border-top: 2px solid var(--rule);
  }

  /* Front side: contact */
  .card-front {
    left: 516px;
    top: 272px;
    width: 578px;
    height: 330px;
  }
  .front-shapes {
    position: absolute;
    inset: 0;
  }
  .person {
    position: absolute;
    left: 22px;
    top: 20px;
    color: var(--paper);
    font-size: 14px;
    line-height: 17px;
    margin: 0;
  }
  .wordmark {
    position: absolute;
    left: 250px;
    top: 132px;
    color: var(--navy);
    font-weight: 700;
    font-size: 30px;
    letter-spacing: 1px;
    margin: 0;
    display: flex;
    align-items: center;
    gap: 10px;
  }
  .wordmark-square {
    width: 16px;
    height: 16px;
    background: var(--orange);
  }
  .contact-line {
    position: absolute;
    left: 22px;
    right: 30px;
    bottom: 20px;
    margin: 0;
    padding-bottom: 6px;
    border-bottom: 1.5px solid var(--grey);
    color: var(--orange);
    font-size: 13px;
    white-space: nowrap;
  }
  .contact-line b { font-weight: 700; margin-left: 14px; }
  .contact-line b:first-child { margin-left: 0; }
</style>
</head>
<body>

<section class="card card-back" aria-label="Card back">
  <div class="back-frame">
    <h2 class="services-title">SECURITY SOLUTION AND SERVICES</h2>
    <ul class="services-list">
      <li>Anti-Virus / Malware</li>
      <li>Anti-Spam Backup / Disaster Recovery</li>
      <li>Email Archiving</li>
      <li>Encryption</li>
      <li>Firewall</li>
      <li>Mobile Security / BYOD</li>
      <li>Network Access Control (NAC)</li>
      <li>Patch Management</li>
      <li>Penetration Testing and Security Assessments</li>
      <li>Virtualization</li>
      <li>Web Filtering</li>
    </ul>
    <div class="back-footer">
      <p class="company-name">HARBOR SHIELD SYSTEMS, INC.</p>
      <address class="company-address">18 Elm Street<br>Riverside, MA 01990</address>
    </div>
    <div class="back-base"></div>
  </div>
</section>

<section class="card card-front" aria-label="Card front">
  <svg class="front-shapes" width="578" height="330" viewBox="0 0 578 330">
    <polygon points="0,0 260,0 118,250 0,250" fill="var(--navy)"/>
    <polygon points="470,0 578,0 578,230" fill="var(--navy)"/>
  </svg>
  <p class="person">Daniel Moreau<br>dmoreau@harborshield.com</p>
  <p class="wordmark"><span class="wordmark-square"></span>Harbor Shield</p>
  <p class="contact-line"><b>Cell:</b> 555.214.7800 <b>Fax:</b> 555.390.1642 <b>Web:</b> www.harborshield.com</p>
</section>

</body>
</html>
```